Ardenwell Building and Property Services needs a business card design

We need a business card design for our building and property services business. We already have a logo we just need a creative design and layout on a business card. Emphasis on clean, modern, professional.
Our client targets are mainly body corporates, building managers, construction managers.
We are a building services company that lean more to structural repair of buildings, through concrete rectification and carbon fibre strengthening.
We also refurbish facades, rendering, painting etc
We target higher end body corporates in prestigious locations, hence why we'd like our cards to reflect professionalism, strength, efficiency

Target Market(s)

body corporates, building managers, construction managers

Industry/Entity Type

Construction

Contact Information for Business Card

Ardenwell is the main word, with 'Building and Property Services' underneath.
Level 17, 82 Harlow Street
MERRIDALE
Melbourne
Vic 3094
T: 9518 2736
Duncan Ferris - Director
dunardenwell@mailbox-example.com

Requirements
Must have
• Stand out on the back of the card- strong/ bold, company logo
• All of the contact details written above
Should not have
• I'd like the card to stand out, especially on the back. Id like the company logo to be prominent, although feel free to be creative around it. But remain clean and professional

```html
<!DOCTYPE html>
<html lang="en">
<head>
<meta charset="utf-8">
<title>Ardenwell Building and Property Services – Business Card</title>
<link rel="stylesheet" href="https://fonts.googleapis.com/css2?family=Cinzel:wght@500;600&family=Open+Sans:wght@400;600&display=swap">
<style>
  :root {
    --page-bg: #e4e5e7;
    --blue-deep: #0a4f97;
    --blue-mid: #1877c9;
    --blue-bright: #2b9be0;
    --blue-brand: #2a8fd6;
    --card-black: #050505;
    --text-white: #ffffff;
    --text-grey: #c9ccd1;
  }
  * { box-sizing: border-box; margin: 0; padding: 0; }
  html, body {
    width: 1200px; height: 900px; overflow: hidden;
    background: var(--page-bg);
  }
  .canvas {
    width: 1200px; height: 900px;
    display: flex; flex-direction: column; align-items: center; justify-content: center;
    gap: 40px;
  }
  .card {
    position: relative;
    width: 700px; height: 400px;
    overflow: hidden;
    box-shadow: 0 6px 18px rgba(0,0,0,0.18);
  }

  /* Front */
  .card-front {
    background: radial-gradient(ellipse at 50% 42%, var(--blue-bright) 0%, var(--blue-mid) 40%, var(--blue-deep) 100%);
    display: flex; flex-direction: column; align-items: center; justify-content: center;
  }
  .front-mark {
    display: flex; align-items: center; gap: 16px;
    margin-top: -10px;
  }
  .mark-square { width: 26px; height: 26px; background: var(--text-white); }
  .front-name {
    font-family: "Cinzel", serif; font-weight: 600;
    font-size: 48px; letter-spacing: 3px; color: var(--text-white);
  }
  .front-web {
    margin-top: 70px;
    font-family: "Open Sans", sans-serif; font-size: 17px;
    letter-spacing: 4px; color: var(--text-white);
  }

  /* Back */
  .card-back { background: var(--card-black); }
  .back-waves { position: absolute; inset: 0; width: 100%; height: 100%; }
  .person {
    position: absolute; top: 34px; right: 58px; text-align: right;
    font-family: "Cinzel", serif; color: var(--text-white);
  }
  .person-name { font-size: 21px; font-weight: 500; letter-spacing: 1px; }
  .person-role { font-size: 14px; color: var(--text-grey); letter-spacing: 1px; margin-top: 2px; }

  .brand {
    position: absolute; left: 70px; top: 150px;
    font-family: "Cinzel", serif; font-weight: 600; color: var(--blue-brand);
  }
  .brand-row { display: flex; align-items: center; gap: 12px; }
  .brand-square { width: 22px; height: 22px; background: var(--blue-brand); }
  .brand-name { font-size: 40px; letter-spacing: 2px; line-height: 1; }
  .brand-tagline { font-size: 9px; letter-spacing: 1.6px; margin-top: 4px; margin-left: 34px; }

  .address {
    position: absolute; left: 70px; top: 258px;
    font-family: "Open Sans", sans-serif; font-size: 16px; line-height: 1.45;
    color: var(--text-white);
  }
  .contacts {
    position: absolute; right: 36px; top: 262px;
    list-style: none; text-align: right;
    font-family: "Open Sans", sans-serif; font-size: 13px; line-height: 1.7;
    color: var(--text-white);
  }
  .contacts li { display: flex; align-items: center; justify-content: flex-end; gap: 7px; }
  .contacts svg { width: 12px; height: 12px; flex: none; }
</style>
</head>
<body>
<main class="canvas">

  <section class="card card-front" aria-label="Card front">
    <div class="front-mark">
      <span class="mark-square"></span>
      <span class="front-name">Ardenwell</span>
    </div>
    <p class="front-web">www.ardenwell-example.com</p>
  </section>

  <section class="card card-back" aria-label="Card back">
    <svg class="back-waves" viewBox="0 0 700 400" preserveAspectRatio="none" aria-hidden="true">
      <defs>
        <linearGradient id="waveBlue" x1="0" y1="1" x2="1" y2="0">
          <stop offset="0" stop-color="#0b5aa8"/>
          <stop offset="0.6" stop-color="#1e88d8"/>
          <stop offset="1" stop-color="#1466b8"/>
        </linearGradient>
        <linearGradient id="waveSilver" x1="0" y1="0" x2="1" y2="0">
          <stop offset="0" stop-color="#7d8288"/>
          <stop offset="0.5" stop-color="#f4f5f7"/>
          <stop offset="1" stop-color="#9da2a8"/>
        </linearGradient>
      </defs>
      <path d="M0,370 C150,383 260,368 334,318 C404,268 484,188 700,108 L700,400 L0,400 Z" fill="url(#waveBlue)"/>
      <path d="M0,362 C150,375 260,360 330,310 C400,260 480,180 700,100" fill="none" stroke="url(#waveSilver)" stroke-width="9"/>
      <path d="M0,375 C155,388 264,373 338,323 C408,273 488,194 700,116" fill="none" stroke="#050505" stroke-width="4"/>
      <path d="M0,398 C200,404 350,392 450,336" fill="none" stroke="url(#waveSilver)" stroke-width="6"/>
    </svg>

    <div class="person">
      <p class="person-name">Duncan Ferris</p>
      <p class="person-role">Director</p>
    </div>

    <div class="brand">
      <div class="brand-row">
        <span class="brand-square"></span>
        <span class="brand-name">Ardenwell</span>
      </div>
      <p class="brand-tagline">Building and Property Services</p>
    </div>

    <p class="address">Level 17, 82 Harlow Street<br>Merridale, Melbourne, Vic 3094</p>

    <ul class="contacts">
      <li>
        <svg viewBox="0 0 12 12"><circle cx="6" cy="6" r="5.4" fill="none" stroke="#fff" stroke-width="1"/><path d="M4 3.5 L5 3.5 L5.5 5 L4.8 5.5 Q5.5 7 6.6 7.4 L7 6.6 L8.5 7.1 L8.5 8.2 Q5 8.6 3.6 4.2 Z" fill="#fff"/></svg>
        <span>9518 2736</span>
      </li>
      <li>
        <svg viewBox="0 0 12 12"><rect x="1" y="3" width="10" height="7" fill="#fff"/><path d="M1 3 L6 7 L11 3" fill="none" stroke="#0b5aa8" stroke-width="1"/></svg>
        <span>dunardenwell@mailbox-example.com</span>
      </li>
      <li>
        <svg viewBox="0 0 12 12"><circle cx="6" cy="6" r="5" fill="none" stroke="#fff" stroke-width="1"/><ellipse cx="6" cy="6" rx="2.2" ry="5" fill="none" stroke="#fff" stroke-width="0.9"/><path d="M1 6 H11" stroke="#fff" stroke-width="0.9"/></svg>
        <span>www.ardenwell-example.com</span>
      </li>
    </ul>
  </section>

</main>
</body>
</html>
```